National Sales Conference

We need a cool one page flyer inviting our sales partners to a National Sales Training Class.

Most important event in 5 years! Do not even consider missing it

Details of Sales Meeting
Nov 10th - 11th in Dallas, TX
Nov 10th (welcome party) 7-9pm

Preliminary Agenda
Nov, 10th 7-9pm Welcome Reception

Nov 11th and 12th 9-4 Tillpoint Drill Week Sales training. Learn the tools you need to become more relevant in the marketplace as we launch multiple new cutting edge products and services. Many vendors will be on hand to personally meet you and provide the tools and marketing information you need.

Location of event
Kelbrook Plaza Lodge West
2876 Harlowmere Pkwy.
Fort Worth, TX 76392
FREE Shuttle from DFW!
Updates

Please put the Brightwater Vendor Solutions logo at the TOP left and the Quillstone Remit logo make it small and near the bottom

Add the following TEXT. 

*** This event is so important our CEO, Marcus Delong has decided that we are covering all of the expenses! That's right, we will provide the sleeping room based on double occupancy, all meals, and with 10 deals in 90 days we will even reimburse your airfare if a flight is necessary. 

Be sure to include the RSVP information and lines for the to print out and check if they are coming or not as indicated in the original brief. 

This flyer will be sent to our sales agents VIA Email in PDF. Therefore, if we need to make it 2 pages so it is not so cluttered, I'm okay with that. 

Target Market(s)

Our Sales Agents

Industry/Entity Type

Training

Requirements
Must have
• One page! High energy will a strong call to action.
• Needs a small fill in the blank for an RSVP
• Name _______________
• Check Box YES! I will gladly attend. _____ # attending
• Check Box Can't make it.
• Fax RSVP to 775-319-2740 or email marcusd@brightwaterco.example

```html
<!DOCTYPE html>
<html lang="en">
<head>
<meta charset="utf-8">
<title>National Sales Training Class</title>
<link href="https://fonts.googleapis.com/css2?family=Goudy+Bookletter+1911&family=Arimo:ital,wght@1,400&display=swap" rel="stylesheet">
<style>
  :root {
    --ink-blue: #4a86b8;
    --brand-green: #4dae1c;
    --banner-green: #3f9f12;
    --navy: #1c2f6b;
    --white: #ffffff;
    --sky-top: #3f6fae;
    --sky-low: #9bb8d6;
    --brick: #9a4a2c;
  }
  html, body {
    margin: 0;
    padding: 0;
    width: 849px;
    height: 1200px;
    overflow: hidden;
    background: var(--white);
  }
  .flyer {
    position: relative;
    width: 849px;
    height: 1200px;
    overflow: hidden;
    background: var(--white);
    font-family: "Goudy Bookletter 1911", Georgia, serif;
    color: var(--ink-blue);
  }
  .hero-photo {
    position: absolute;
    left: 0; top: 0;
    width: 849px; height: 415px;
    background: linear-gradient(180deg, var(--sky-top) 0%, var(--sky-low) 38%, #c7895f 55%, var(--brick) 72%, #6d3a24 86%, #56604a 100%);
  }
  .brand-logo {
    position: absolute;
    left: 21px; top: 14px;
    width: 299px; height: 109px;
    background: var(--white);
    display: flex;
    align-items: center;
    gap: 12px;
    padding: 0 16px;
    box-sizing: border-box;
  }
  .brand-logo .mark {
    width: 34px; height: 34px;
    background: var(--banner-green);
    flex: none;
  }
  .brand-logo .name {
    font-size: 28px;
    line-height: 1.05;
    color: var(--navy);
  }
  .tagline-ribbon {
    position: absolute;
    left: 168px; top: 332px;
    width: 570px; height: 96px;
  }
  .tagline-ribbon p {
    position: absolute;
    left: 0; right: 0;
    margin: 0;
    text-align: center;
    font-family: "Arimo", Arial, sans-serif;
    font-style: italic;
    color: var(--white);
  }
  .tagline-ribbon .line-1 { top: 22px; font-size: 23px; }
  .tagline-ribbon .line-2 { top: 51px; font-size: 25px; }
  .centered {
    position: absolute;
    left: 0; right: 0;
    margin: 0;
    text-align: center;
  }
  .invite { top: 442px; font-size: 20px; left: 40px; right: 0; }
  .event-title { top: 472px; font-size: 48px; color: var(--brand-green); font-weight: 400; left: 76px; right: 0; }
  .on { top: 527px; font-size: 20px; left: 40px; }
  .dates { top: 567px; font-size: 22px; left: 50px; }
  .agenda-heading { top: 596px; font-size: 28px; font-weight: 400; text-decoration: underline; text-underline-offset: 4px; left: 40px; }
  .agenda-row {
    position: absolute;
    left: 0;
    font-size: 21px;
    display: flex;
    white-space: nowrap;
  }
  .agenda-row .day { width: 245px; text-align: right; }
  .agenda-row .time { margin-left: 42px; }
  .agenda-row .item { margin-left: 18px; }
  .row-1 { top: 654px; }
  .row-2 { top: 698px; }
  .row-2 .time { margin-left: 47px; }
  .training-copy {
    position: absolute;
    left: 288px; top: 748px;
    width: 505px;
    margin: 0;
    font-size: 21.5px;
    line-height: 26px;
  }
  .special-note {
    position: absolute;
    left: 21px; top: 916px;
    width: 800px;
    margin: 0;
    display: flex;
    font-style: italic;
    font-size: 18.5px;
    line-height: 26px;
    color: var(--brand-green);
  }
  .special-note .label { width: 75px; flex: none; }
  .special-note .body { width: 715px; }
  .rsvp { top: 1010px; font-size: 21px; left: 20px; }
  .rsvp-form {
    position: absolute;
    left: 0; right: 0; top: 1050px;
    display: flex;
    justify-content: center;
    align-items: flex-end;
    gap: 8px;
    font-size: 17px;
    white-space: nowrap;
  }
  .rsvp-form .blank {
    display: inline-block;
    border-bottom: 1px solid var(--ink-blue);
    height: 17px;
  }
  .rsvp-form .blank.name { width: 170px; margin-right: 16px; }
  .rsvp-form .blank.count { width: 44px; }
  .rsvp-form .box {
    display: inline-block;
    width: 13px; height: 13px;
    border: 1.5px solid var(--ink-blue);
    margin-bottom: 2px;
  }
  .rsvp-form .gap { margin-left: 16px; }
  .venue {
    position: absolute;
    left: 19px; top: 1101px;
    margin: 0;
    font-size: 15px;
    line-height: 21px;
    font-style: normal;
  }
  .shuttle {
    position: absolute;
    left: 292px; top: 1155px;
    margin: 0;
    font-size: 25px;
    font-style: italic;
    color: var(--brand-green);
  }
  .partner-logo {
    position: absolute;
    left: 636px; top: 1098px;
    width: 190px; height: 90px;
    display: flex;
    align-items: center;
    justify-content: center;
    gap: 10px;
  }
  .partner-logo .mark {
    width: 22px; height: 22px;
    border-radius: 50%;
    background: var(--ink-blue);
    flex: none;
  }
  .partner-logo .name {
    font-size: 22px;
    color: var(--ink-blue);
  }
</style>
</head>
<body>
<main class="flyer">
  <div class="hero-photo" role="img" aria-label="Dusk photograph of the brick hotel venue with a covered entrance, flagpoles and a shuttle van"></div>

  <div class="brand-logo">
    <span class="mark"></span>
    <span class="name">Brightwater Vendor Solutions</span>
  </div>

  <div class="tagline-ribbon">
    <svg width="570" height="96" viewBox="0 0 570 96" aria-hidden="true">
      <defs>
        <linearGradient id="ribbonFill" x1="0" y1="0" x2="0" y2="1">
          <stop offset="0" stop-color="#86d640"/>
          <stop offset="0.55" stop-color="#4aaa17"/>
          <stop offset="1" stop-color="#2f8a0b"/>
        </linearGradient>
      </defs>
      <path d="M0 92 C40 92 60 78 70 40 C76 14 96 8 130 8 L440 8 C474 8 494 14 500 40 C510 78 530 92 570 92 Z" fill="url(#ribbonFill)"/>
    </svg>
    <p class="line-1">Most important event in 5 years!</p>
    <p class="line-2">Do not even consider missing it</p>
  </div>

  <p class="centered invite">You are cordially invited to</p>
  <h1 class="centered event-title">National Sales Training Class.</h1>
  <p class="centered on">on</p>
  <p class="centered dates">Nov 10th&nbsp; to 12th 2013 in Dallas, TX</p>
  <h2 class="centered agenda-heading">Agenda</h2>

  <div class="agenda-row row-1">
    <span class="day">Nov 10th 2013</span>
    <span class="time">7 to 9 pm</span>
    <span class="item">Welcome Reception</span>
  </div>
  <div class="agenda-row row-2">
    <span class="day">Nov 11th &amp; 12th 2013</span>
    <span class="time">9 to 4 pm</span>
    <span class="item">Tillpoint Drill Week Sales training.</span>
  </div>

  <p class="training-copy">Learn the tools you need to become more relevant in the marketplace as we launch multiple new cutting edge products and services. Many vendors will be on hand to personally meet you and provide the tools and marketing information you need.</p>

  <p class="special-note">
    <span class="label">Special :</span>
    <span class="body">This event is so important our CEO, Marcus Delong has decided that we are covering&nbsp; all of the expenses! That's right, we will provide the sleeping room based on double&nbsp; occupancy, all meals, and with 10 deals in 90 days we will even reimburse your&nbsp; airfare if a flight is necessary.</span>
  </p>

  <p class="centered rsvp">Fax RSVP to 775-319-2740 or email marcusd@brightwaterco.example</p>

  <div class="rsvp-form">
    <span>Name</span><span class="blank name"></span>
    <span class="box"></span><span>YES! I will gladly attend.</span>
    <span class="blank count"></span><span># attending</span>
    <span class="box gap"></span><span>Can't make it.</span>
  </div>

  <address class="venue">
    Location of event<br>
    Kelbrook Plaza Lodge West<br>
    2876 Harlowmere Pkwy.<br>
    Fort Worth, TX 76392
  </address>

  <p class="shuttle">FREE Shuttle from DFW!</p>

  <div class="partner-logo">
    <span class="mark"></span>
    <span class="name">Quillstone Remit</span>
  </div>
</main>
</body>
</html>
```